Geschäftspapiere für Rechtsberatung
Zielgruppe
Rechtsberatung; Zielgruppe sind sowohl Privat- als auch Geschäftsleute
Die Einzelkanzlei von Greta Münzberg (Näheres siehe www.muenzberg-kanzlei.de) wird zu einer Partnergesellschaft, der
Münzberg

```html
<!DOCTYPE html>
<html lang="de">
<head>
<meta charset="utf-8">
<title>Briefbogen – Rechtsanwaltskanzlei Greta Münzberg</title>
<link rel="stylesheet" href="https://fonts.googleapis.com/css2?family=Crimson+Pro:wght@400;700&family=Open+Sans:wght@400&display=swap">
<style>
  :root {
    --canvas: #f1f1f1;
    --paper: #ffffff;
    --band: #a7a8ab;
    --footer: #d9dadc;
    --accent: #9b1b1f;
    --ink: #1d1d1d;
    --ink-soft: #555557;
    --ink-muted: #77787a;
    --fold: #9a9a9a;
  }
  * { margin: 0; padding: 0; box-sizing: border-box; }
  html, body {
    width: 1200px; height: 861px; overflow: hidden;
    background: var(--canvas);
  }
  .letterhead {
    position: absolute; left: 302px; top: 9px;
    width: 596px; height: 843px;
    background: var(--paper);
    box-shadow: 0 1px 4px rgba(0,0,0,.12);
    font-family: "Crimson Pro", Georgia, serif;
    color: var(--ink);
    overflow: hidden;
  }
  .top-band { position: absolute; left: 0; top: 0; }
  .firm-heading {
    position: absolute; left: 0; width: 100%; top: 92px;
    text-align: center;
  }
  .firm-heading__type {
    font-family: "Open Sans", Arial, sans-serif;
    font-size: 10px; color: var(--ink);
    display: block; line-height: 12px;
  }
  .firm-heading__name {
    font-size: 16px; color: var(--ink-soft);
    display: block; line-height: 20px; letter-spacing: .3px;
  }
  .sender-line {
    position: absolute; left: 56px; top: 155px;
    font-size: 8px; color: var(--ink); white-space: nowrap;
  }
  .sender-line__firm { color: var(--accent); font-weight: 700; }
  .reference {
    position: absolute; left: 393px; top: 153px;
    font-size: 10px; color: var(--ink-muted); line-height: 17px;
  }
  .fold-mark { position: absolute; height: 1px; background: var(--fold); }
  .fold-mark--upper { left: 0; top: 297px; width: 8px; }
  .fold-mark--punch { left: 33px; top: 420px; width: 17px; }
  .fold-mark--lower { left: 0; top: 594px; width: 8px; }
  .footer {
    position: absolute; left: 0; bottom: 0;
    width: 100%; height: 112px;
    background: var(--footer);
    font-size: 10px; line-height: 14px; color: var(--ink-muted);
  }
  .footer p { white-space: nowrap; }
  .footer__col { position: absolute; top: 16px; }
  .footer__col--office { left: 56px; }
  .footer__col--contact { left: 254px; }
  .footer__col--bank { left: 410px; }
  .footer__strong { color: var(--ink); font-weight: 700; }
  .footer__gap { height: 6px; }
  .footer__row { display: flex; }
  .footer__label { flex: 0 0 34px; }
  .footer__label--wide { flex: 0 0 54px; }
</style>
</head>
<body>
  <main class="letterhead">
    <svg class="top-band" width="596" height="80" viewBox="0 0 596 80" aria-hidden="true">
      <rect x="0" y="0" width="596" height="38" fill="var(--band)"/>
      <polygon points="250,38 276,10 318,10 344,38" fill="var(--paper)"/>
      <rect x="274" y="30" width="44" height="44" fill="var(--accent)"/>
    </svg>

    <header class="firm-heading">
      <span class="firm-heading__type">Rechtsanwaltskanzlei</span>
      <span class="firm-heading__name">Greta Münzberg</span>
    </header>

    <p class="sender-line"><span class="sender-line__firm">Münzberg § Rosenthal PartG mbB</span> • Talstr. 21 • 45525 Wiesental</p>

    <div class="reference">
      <p>Datum:</p>
      <p>Unser Zeichen:</p>
    </div>

    <span class="fold-mark fold-mark--upper"></span>
    <span class="fold-mark fold-mark--punch"></span>
    <span class="fold-mark fold-mark--lower"></span>

    <footer class="footer">
      <div class="footer__col footer__col--office">
        <p class="footer__strong">Münzberg § Rosenthal PartG mbB</p>
        <p class="footer__strong">Greta Münzberg</p>
        <div class="footer__gap"></div>
        <p>Dipl.-Juristin</p>
        <p>Talstr. 21</p>
        <p>45525 Wiesental</p>
      </div>
      <div class="footer__col footer__col--contact">
        <p class="footer__row"><span class="footer__label">Tel.:</span>02324/5512400</p>
        <p class="footer__row"><span class="footer__label">Fax:</span>02324/5512402</p>
        <p class="footer__row"><span class="footer__label">Mobil:</span>0177/5512403</p>
        <div class="footer__gap"></div>
        <p class="footer__row"><span class="footer__label">Mail:</span>info@muenzberg.de</p>
        <p class="footer__row"><span class="footer__label">Web:</span>www.muenzberg-kanzlei.de</p>
      </div>
      <div class="footer__col footer__col--bank">
        <p>NRB Bank</p>
        <p class="footer__row"><span class="footer__label footer__label--wide">IBAN:</span>DE0012345000</p>
        <p class="footer__row"><span class="footer__label footer__label--wide"></span>0000111222</p>
        <p class="footer__row"><span class="footer__label footer__label--wide">BIC:</span>NRBADE33 000</p>
        <div class="footer__gap"></div>
        <p class="footer__row"><span class="footer__label footer__label--wide">Steuer-Nr.</span>XXX XXX XXX XXX</p>
      </div>
    </footer>
  </main>
</body>
</html>
```